Law Office business card design

I have a general practice specializing in criminal defense work and domestic cases. I have extensive trial and appellate experience.

Target Market(s)

general public

Industry/Entity Type

Defense

Contact Information for Business Card

Darrowby Law Office, P.A.
382 N. 4th
PO Box 5274
Salina, KS 67409-5274
(785) 555-0172
(785) 555-0198 FAX
tdarrow@plinkmail.example

Requirements
Must have
• A symbol that immediately identifes the card as a legal practice.

```html
<!DOCTYPE html>
<html lang="en">
<head>
<meta charset="utf-8">
<title>Darrowby Law Office – Business Card</title>
<link rel="stylesheet" href="https://fonts.googleapis.com/css2?family=Questrial&display=swap">
<style>
  :root {
    --backdrop: #d9d9d9;
    --card: #ffffff;
    --brand-red: #c8232c;
    --ink: #1c1c1c;
    --muted-line: #9a9a9a;
    --ring: #3a3a3a;
  }
  html, body {
    margin: 0;
    padding: 0;
    width: 1200px;
    height: 900px;
    overflow: hidden;
    background: var(--backdrop);
    font-family: "Questrial", "Century Gothic", sans-serif;
  }
  .canvas {
    position: relative;
    width: 1200px;
    height: 900px;
  }
  .business-card {
    position: absolute;
    left: 75px;
    top: 150px;
    width: 1050px;
    height: 600px;
    background: var(--card);
    box-shadow: 0 6px 24px rgba(0,0,0,0.18);
    display: flex;
  }
  .brand-block {
    width: 470px;
    display: flex;
    flex-direction: column;
    align-items: center;
    justify-content: center;
    gap: 34px;
  }
  .brand-disc {
    width: 190px;
    height: 190px;
    border-radius: 50%;
    background: var(--brand-red);
    box-shadow: 0 0 0 6px var(--card), 0 0 0 9px var(--ring);
  }
  .brand-name {
    margin: 0;
    text-align: center;
    color: var(--ink);
    font-size: 40px;
    letter-spacing: 6px;
    line-height: 1.2;
    font-weight: 400;
    text-transform: uppercase;
  }
  .divider {
    width: 2px;
    background: var(--muted-line);
    margin: 100px 0 60px;
  }
  .contact-block {
    padding: 100px 0 0 50px;
  }
  .person-name {
    margin: 0;
    color: var(--brand-red);
    font-size: 40px;
    font-weight: 400;
  }
  .person-role {
    margin: 2px 0 50px;
    color: var(--ink);
    font-size: 34px;
  }
  .contact-list {
    list-style: none;
    margin: 0;
    padding: 0;
  }
  .contact-item {
    display: flex;
    align-items: flex-start;
    gap: 22px;
    margin-bottom: 26px;
    color: var(--ink);
    font-size: 28px;
    line-height: 36px;
  }
  .contact-icon {
    flex: none;
    width: 36px;
    height: 36px;
  }
</style>
</head>
<body>
<div class="canvas">
  <article class="business-card">
    <section class="brand-block">
      <div class="brand-disc" aria-hidden="true"></div>
      <h1 class="brand-name">Darrowby<br>Law Office</h1>
    </section>
    <div class="divider" aria-hidden="true"></div>
    <section class="contact-block">
      <h2 class="person-name">Tessa Darrowby</h2>
      <p class="person-role">Lawyer</p>
      <ul class="contact-list">
        <li class="contact-item">
          <svg class="contact-icon" viewBox="0 0 36 36" aria-hidden="true">
            <circle cx="18" cy="18" r="16" fill="none" stroke="var(--brand-red)" stroke-width="2.5"/>
            <path d="M12 10 l4 -1 l2 5 l-2.5 2 q2 4 5 5 l2 -2.5 l5 2 l-1 4 q-10 1 -14.5 -14.5z" fill="var(--brand-red)"/>
          </svg>
          <span>(785) 555-0172</span>
        </li>
        <li class="contact-item">
          <svg class="contact-icon" viewBox="0 0 36 36" aria-hidden="true">
            <circle cx="18" cy="18" r="16" fill="none" stroke="var(--brand-red)" stroke-width="2.5"/>
            <rect x="12" y="9" width="12" height="7" fill="none" stroke="var(--brand-red)" stroke-width="2"/>
            <rect x="9" y="16" width="18" height="8" rx="1.5" fill="var(--brand-red)"/>
            <rect x="12" y="22" width="12" height="5" fill="#fff" stroke="var(--brand-red)" stroke-width="2"/>
          </svg>
          <span>(785) 555-0198</span>
        </li>
        <li class="contact-item">
          <svg class="contact-icon" viewBox="0 0 36 36" aria-hidden="true">
            <circle cx="18" cy="18" r="16" fill="none" stroke="var(--brand-red)" stroke-width="2.5"/>
            <rect x="9" y="12" width="18" height="12" fill="none" stroke="var(--brand-red)" stroke-width="2"/>
            <path d="M9 12 l9 7 l9 -7" fill="none" stroke="var(--brand-red)" stroke-width="2"/>
          </svg>
          <span>tdarrow@plinkmail.example</span>
        </li>
        <li class="contact-item">
          <svg class="contact-icon" viewBox="0 0 36 36" aria-hidden="true">
            <circle cx="18" cy="18" r="16" fill="none" stroke="var(--brand-red)" stroke-width="2.5"/>
            <path d="M18 28 q-7 -8 -7 -12.5 a7 7 0 0 1 14 0 q0 4.5 -7 12.5z" fill="var(--brand-red)"/>
            <circle cx="18" cy="15.5" r="2.6" fill="#fff"/>
          </svg>
          <span>P.A. 382 N. 4th PO Box 5274<br>Salina, KS 67409-5274</span>
        </li>
      </ul>
    </section>
  </article>
</div>
</body>
</html>
```